ZUMRA Virtualizing the computer, making it live in the cloud

We plan to visualize the computer, essentially making all your computing, storage, security, processing, etc done in the cloud. We feel this will revolutionize the entire computer industry.
We have a logo design which has been included here. We want this sharp, progressive and also frameworked in a way that we can sell our monthly service as well as computers online through this site.

Target Market(s)

Laptop users, Millennials, college educated people.

Industry/Entity Type

Computer

Number of Pages Required

5+ page

Font styles to use
Serif
Sans Serif

Colors

Designer to choose colors to be used in the design.

Requirements
Must have
• eCommerce capable. Frameworked for people to enroll in our program and pay for the service online. Would prefer to allow people from multiple countries to enroll and use our service

```html
<!DOCTYPE html>
<html lang="en">
<head>
<meta charset="utf-8">
<title>ZUMRA – Cloud Computing</title>
<link href="https://fonts.googleapis.com/css2?family=Nunito+Sans:wght@400;600;700&family=Open+Sans:ital,wght@0,400;0,600;1,400&family=Lato:wght@400;700&display=swap" rel="stylesheet">
<style>
:root{
  --yellow:#fcc21b;
  --dark:#141414;
  --ink:#2b2b2b;
  --muted:#9a9a9a;
  --white:#ffffff;
  --tech-panel:#6e6e6e;
  --why-bg:#9b9b9b;
  --footer:#1b1b1b;
}
*{margin:0;padding:0;box-sizing:border-box}
html,body{width:1200px;height:3364px;overflow:hidden}
body{position:relative;background:var(--white);font-family:"Open Sans",sans-serif;color:var(--ink)}
.abs{position:absolute}
h2,.nav,.brand{font-family:"Nunito Sans",sans-serif}

/* hero */
.hero{left:0;top:0;width:1200px;height:691px;background:linear-gradient(100deg,#1c1a17 0%,#3b2f22 35%,#6a5038 60%,#2a2420 100%)}
.hero-photo{left:0;top:0;width:1200px;height:691px;background:radial-gradient(ellipse at 70% 45%,rgba(230,170,110,.45),rgba(0,0,0,0) 55%),linear-gradient(180deg,rgba(0,0,0,.45),rgba(0,0,0,0) 30%)}
.brand{color:var(--white);font-weight:700;font-size:46px;letter-spacing:1px;display:flex;align-items:center;gap:12px}
.brand .dot{width:18px;height:18px;border-radius:50%;background:var(--yellow)}
.hero .brand{left:119px;top:46px}
.nav{top:62px;left:406px;display:flex;gap:0;width:680px;justify-content:space-between;font-size:17px;font-weight:700;color:var(--white)}
.nav .active{color:var(--yellow)}
.hero-title{left:130px;top:292px;font-family:"Nunito Sans",sans-serif;font-weight:700;font-size:45px;line-height:48px;color:var(--white)}
.hero-title span{color:var(--yellow);display:block}
.hero-text{left:132px;top:403px;width:420px;font-size:15px;line-height:27px;color:#eee}
.dots{left:516px;top:658px;display:flex;gap:8px}
.dots i{display:block;width:32px;height:5px;background:var(--white)}
.dots i.on{background:var(--yellow)}

/* company */
.section-title{width:1200px;text-align:center;font-weight:400;font-size:34px;color:var(--dark)}
.company-title{top:780px}
.rule{left:500px;width:200px;height:14px}
.company-text{left:200px;top:857px;width:800px;text-align:center;font-size:15.5px;line-height:34px;color:var(--muted)}

/* technology */
.tech-photo{left:0;top:1121px;width:691px;height:474px;background:linear-gradient(120deg,#5b4a35,#8a7356 35%,#2e2c2a 70%,#4c4a47)}
.tech-panel{left:691px;top:1121px;width:509px;height:474px;background:linear-gradient(90deg,#5d5d5d,var(--tech-panel) 50%,#777)}
.tech-panel h2{position:absolute;left:42px;top:88px;font-weight:600;font-size:33px;color:var(--white)}
.tech-panel .lead{position:absolute;left:42px;top:143px;width:420px;font-size:14.5px;line-height:25px;color:var(--white)}
.tech-panel .body{position:absolute;left:42px;top:198px;width:430px;font-size:13.5px;line-height:28px;color:#f1f1f1}
.btn{display:inline-block;border:2px solid var(--white);color:var(--white);font-size:14px;letter-spacing:.5px;padding:8px 22px}
.tech-panel .btn{position:absolute;left:42px;top:338px}

/* services */
.services{left:0;top:1595px;width:1200px;height:446px;background:var(--yellow);overflow:hidden}
.services h2{position:absolute;top:44px;width:1200px;text-align:center;font-weight:400;font-size:33px;color:var(--white)}
.svc{position:absolute;color:var(--white)}
.svc b{display:block;font-family:"Nunito Sans",sans-serif;font-weight:600;font-size:21px}
.svc p{font-size:12.5px;line-height:17px;color:#fff6d6;width:230px}
.svc.r{text-align:right}
.svc.r p{margin-left:auto}
.services .mark{position:absolute;left:0;top:330px;width:1200px;text-align:center;font-family:"Nunito Sans",sans-serif;font-weight:700;font-size:80px;color:rgba(255,255,255,.35)}

/* why */
.why{left:0;top:2041px;width:1200px;height:426px;background:var(--why-bg)}
.why h2{position:absolute;left:112px;top:74px;font-weight:600;font-size:34px;color:var(--white)}
.why .lead{position:absolute;left:112px;top:135px;width:440px;font-size:16px;line-height:27px;color:var(--white)}
.why .body{position:absolute;left:112px;top:195px;width:460px;font-size:14.5px;line-height:29px;color:#f3f3f3}
.why .btn{position:absolute;left:116px;top:294px}
.why-art{position:absolute;left:594px;top:56px;width:494px;height:281px;border-radius:6px;background:radial-gradient(ellipse at 50% 45%,#ffffff,#dcdcdc 55%,rgba(190,190,190,.3) 80%)}

/* testimonials */
.clients{left:0;top:2467px;width:1200px;height:449px;background:linear-gradient(#fff,#f6f6f6)}
.clients h2{position:absolute;top:50px;width:1200px;text-align:center;font-weight:600;font-size:30px;color:var(--dark)}
.quote-box{position:absolute;left:296px;top:148px;width:604px;height:207px;border:3px solid var(--yellow);background:var(--white);box-shadow:0 6px 14px rgba(0,0,0,.12)}
.quote-box q{position:absolute;left:70px;top:50px;width:464px;text-align:center;font-style:italic;font-size:15px;line-height:28px;color:var(--muted);quotes:none}
.quote-box .qm{position:absolute;font-family:"Open Sans",serif;font-size:44px;color:var(--ink);line-height:1}
.quote-box cite{position:absolute;top:152px;width:100%;text-align:center;font-style:normal;font-size:15px;color:#555}
.avatar{position:absolute;left:561px;top:110px;width:76px;height:76px;border-radius:50%;border:4px solid var(--yellow);background:radial-gradient(circle at 50% 45%,#c9c9c9,#7b6a52)}

/* footer */
.footer{left:0;top:2916px;width:1200px;height:448px;background:radial-gradient(ellipse at 75% 40%,#333,var(--footer) 60%)}
.fcol{position:absolute;top:80px;font-family:"Lato",sans-serif}
.fcol h3{font-weight:400;font-size:20px;color:var(--yellow);margin-bottom:10px}
.fcol li{list-style:none;font-size:14.5px;line-height:31px;color:#e6e6e6}
.social{display:flex;gap:8px;margin-top:10px}
.social i{display:block;width:28px;height:28px;border-radius:50%;border:1.5px solid #ddd}
.footer .brand{left:848px;top:104px;font-size:52px}
.footer .line{position:absolute;left:121px;top:370px;width:958px;height:1px;background:#444}
.copy{position:absolute;top:394px;width:1200px;text-align:center;font-family:"Lato",sans-serif;font-size:12px;color:#888}
</style>
</head>
<body>

<header class="abs hero">
  <div class="abs hero-photo" role="img" aria-label="Photo of a hand touching a tablet with a glowing cloud network overlay"></div>
  <div class="abs brand"><span class="dot"></span>ZUMRA</div>
  <nav class="abs nav"><span class="active">Home</span><span>About Us</span><span>Our Services</span><span>Cloud Storage</span><span>Clients</span><span>Contact</span></nav>
  <h1 class="abs hero-title"><span>Cloud Computing</span>Storage &amp; Security</h1>
  <p class="abs hero-text">Proin nulla arcu nonummy luctus dictum eget fermentum et lorem. Nunc porta convallis pede</p>
  <div class="abs dots"><i></i><i></i><i class="on"></i><i></i></div>
</header>

<section>
  <h2 class="abs section-title company-title">Our Company</h2>
  <svg class="abs rule" style="top:832px" viewBox="0 0 200 14"><line x1="0" y1="3" x2="200" y2="3" stroke="#ccc" stroke-width="1.5"/><polyline points="86,3 100,11 114,3" fill="none" stroke="#999" stroke-width="2"/></svg>
  <p class="abs company-text">Maecenas aliquet velit vel turpis Mauris neque metus malesuada nec ultricies sit amet porttitor mattis enim In massa libero interdum nec interdum vel blandit sed nulla In ullamcorper est eget tempor cursus neque mi consectetuer mi a ultricies massa est sed nisl</p>
  <svg class="abs" style="left:580px;top:985px" width="40" height="24" viewBox="0 0 40 24"><polyline points="3,4 20,19 37,4" fill="none" stroke="#bbb" stroke-width="5"/></svg>
</section>

<section>
  <div class="abs tech-photo" role="img" aria-label="Photo of a person with a tablet beside a laptop showing cloud connection icons"></div>
  <div class="abs tech-panel">
    <h2>Our Technology</h2>
    <p class="lead">Maecenas aliquet velit vel turpis Mauris neque metus malesuada nec ultricies sit</p>
    <p class="body">mattis enim In massa libero interdum nec interdum vel blandit sed nulla In ullamcorper est eget tempor cursus neque mi consectetuer mi a ultricies massa est sed nisl Class aptent taciti sociosqu ad litora torque</p>
    <span class="btn">READ MORE</span>
  </div>
</section>

<section class="abs services">
  <h2>Our Services</h2>
  <svg class="abs" style="left:0;top:0" width="1200" height="446" viewBox="0 0 1200 446">
    <line x1="490" y1="100" x2="710" y2="100" stroke="#fff" stroke-width="1.5"/>
    <polyline points="587,100 599,107 611,100" fill="#fff" stroke="#fff"/>
    <circle cx="599" cy="345" r="213" fill="none" stroke="#fff" stroke-width="2.5"/>
    <circle cx="599" cy="385" r="118" fill="rgba(255,255,255,.12)"/>
    <g fill="none" stroke="#fff" stroke-width="2">
      <path d="M418 207a9 9 0 0 1 8-12a12 12 0 0 1 22 4a8 8 0 0 1 0 16h-28a8 8 0 0 1-2-8z"/>
      <rect x="744" y="188" width="24" height="7"/><rect x="744" y="198" width="24" height="7"/><rect x="744" y="208" width="24" height="7"/>
      <path d="M330 346a9 9 0 0 1 8-12a12 12 0 0 1 22 4a8 8 0 0 1 0 16h-28a8 8 0 0 1-2-8z"/><line x1="345" y1="355" x2="345" y2="343"/><polyline points="340,347 345,342 350,347"/>
      <path d="M828 356a9 9 0 0 1 8-12a12 12 0 0 1 22 4a8 8 0 0 1 0 16h-28a8 8 0 0 1-2-8z"/><rect x="838" y="352" width="10" height="9"/>
    </g>
  </svg>
  <div class="svc r" style="left:158px;top:166px;width:230px"><b>Cloud Computing</b><p>Pellentesque habitant morbi tristique senectus et netus et malesuada</p></div>
  <div class="svc" style="left:787px;top:166px"><b>Our Server</b><p>Pellentesque habitant morbi tristique senectus et netus et malesuada</p></div>
  <div class="svc r" style="left:78px;top:300px;width:240px"><b>Cloud Storage</b><p>Pellentesque habitant morbi tristique senectus et netus et malesuada</p></div>
  <div class="svc" style="left:877px;top:312px"><b>Cloud Security</b><p>Pellentesque habitant morbi tristique senectus et netus et malesuada</p></div>
  <div class="mark">ZUMRA</div>
</section>

<section class="abs why">
  <h2>Why We Are</h2>
  <p class="lead">Maecenas aliquet velit vel turpis Mauris neque metus malesuada nec ultricies sit amet porttitor</p>
  <p class="body">mattis enim In massa libero interdum nec interdum vel blandit sed nulla In ullamcorper est eget tempor cursus neque mi consectetuer mi a ultricies massa est sed nisl</p>
  <span class="btn">READ MORE</span>
  <div class="why-art" role="img" aria-label="Illustration of a cloud connected to laptops, phones and data icons"></div>
</section>

<section class="abs clients">
  <h2>What Our Client Says</h2>
  <div class="quote-box">
    <span class="qm" style="left:48px;top:40px">“</span>
    <q>Curabitur iaculis tempus eros Curabitur vel mi sit amet magna malesuada ultrices . Morbi ornare gravida elit Integer congue augue et malesuada iaculis ipsum dui aliqu</q>
    <span class="qm" style="right:48px;top:40px">”</span>
    <cite>By Author Name</cite>
  </div>
  <div class="avatar" role="img" aria-label="Client portrait"></div>
  <svg class="abs" style="left:252px;top:214px" width="28" height="60" viewBox="0 0 28 60"><polyline points="24,2 4,30 24,58" fill="none" stroke="#999" stroke-width="2"/></svg>
  <svg class="abs" style="left:920px;top:214px" width="28" height="60" viewBox="0 0 28 60"><polyline points="4,2 24,30 4,58" fill="none" stroke="#999" stroke-width="2"/></svg>
</section>

<footer class="abs footer">
  <div class="fcol" style="left:121px"><h3>COMPANY</h3><ul><li>Home</li><li>About Us</li><li>Cloud Services</li><li>Our Technology</li><li>Why Use</li></ul></div>
  <div class="fcol" style="left:339px"><h3>RESOURCES</h3><ul><li>Support</li><li>FAQ</li><li>Tesimonials</li><li>Clients</li><li>Contact Us</li></ul></div>
  <div class="fcol" style="left:545px"><h3>CONTACT US</h3><ul><li>418 Meridian Park Road Suite B20</li><li>Halden, PA 19311</li><li>(555) 014-2270</li><li>hello@zumra-mail.com</li></ul>
    <div class="social"><i></i><i></i><i></i><i></i><i></i></div></div>
  <div class="abs brand"><span class="dot"></span>ZUMRA</div>
  <div class="line"></div>
  <p class="copy">© 2017 Company Name  All right reserved  Term of Use</p>
</footer>

</body>
</html>
```